Ruler design for Harrowby Liquid waste

We require a very professional design for our marketing product 'Ruler'.
It will be on a white plastic ruler 315mm long and 39mm high.
0 – 30 on the top (in mm).
0 – 12 on the bottom (in inches).
Numbering in black (to be included as an example only) as it is already printed on the plastic stock.
I want logo, phone number, email and website.
Phone number - 08 8371 4925, email info@hdw.com.au, web www.harrowbyliquidwaste.com
Large text - Your Local Grease Trap and Liquid Waste Specialists
Please stick to our colours.
Total workable text area –
Length 312mm
Height 24mm
You must supply Print ready pdf files with
all fonts embedded.
Please include crop marks plus 3mm bleed all round.

```html
<!DOCTYPE html>
<html lang="en">
<head>
<meta charset="utf-8">
<title>Harrowby Liquid waste – Ruler</title>
<link href="https://fonts.googleapis.com/css2?family=Bebas+Neue&family=Open+Sans:wght@400;600;700&display=swap" rel="stylesheet">
<style>
  :root{
    --page:#e9e9e9;
    --ruler:#ffffff;
    --scale:#1a1a1a;
    --headline:#d8332a;
    --brand-navy:#101a5e;
    --brand-orange:#e8541c;
    --icon-yellow:#f3d20c;
    --panel-text:#ffffff;
  }
  html,body{margin:0;padding:0;overflow:hidden;}
  body{width:1200px;height:900px;background:var(--page);display:flex;align-items:center;justify-content:center;}
  .ruler{width:1120px;height:140px;display:block;box-shadow:0 2px 6px rgba(0,0,0,.18);}
  .ruler__body{fill:var(--ruler);}
  .scale-num{font-family:"Open Sans",sans-serif;font-size:11px;fill:var(--scale);text-anchor:middle;}
  .scale-num--inch{font-size:13px;}
  .headline{font-family:"Bebas Neue",sans-serif;font-size:36px;fill:var(--headline);letter-spacing:.5px;}
  .contact-panel{fill:var(--brand-navy);}
  .brand-mark{fill:var(--brand-orange);}
  .brand-name{font-family:"Open Sans",sans-serif;font-weight:700;font-size:11px;fill:var(--panel-text);letter-spacing:.5px;text-anchor:middle;}
  .contact-text{font-family:"Open Sans",sans-serif;font-size:11px;fill:var(--panel-text);}
  .contact-icon{fill:var(--icon-yellow);}
  .contact-icon-detail{fill:none;stroke:var(--brand-navy);stroke-width:.9;}
</style>
</head>
<body>
<svg class="ruler" viewBox="0 0 1120 140" role="img" aria-label="Harrowby Liquid waste promotional ruler">
  <defs>
    <pattern id="mm-tick" patternUnits="userSpaceOnUse" x="8" y="0" width="3.556" height="140">
      <rect x="0" y="0" width="0.8" height="6" fill="#1a1a1a"/>
    </pattern>
    <pattern id="half-cm-tick" patternUnits="userSpaceOnUse" x="8" y="0" width="17.78" height="140">
      <rect x="0" y="0" width="0.9" height="9" fill="#1a1a1a"/>
    </pattern>
    <pattern id="cm-tick" patternUnits="userSpaceOnUse" x="8" y="0" width="35.56" height="140">
      <rect x="0" y="0" width="1" height="13" fill="#1a1a1a"/>
    </pattern>
    <pattern id="sixteenth-tick" patternUnits="userSpaceOnUse" x="10" y="0" width="5.645" height="140">
      <rect x="0" y="134" width="0.7" height="6" fill="#1a1a1a"/>
    </pattern>
    <pattern id="eighth-tick" patternUnits="userSpaceOnUse" x="10" y="0" width="11.29" height="140">
      <rect x="0" y="131" width="0.8" height="9" fill="#1a1a1a"/>
    </pattern>
    <pattern id="quarter-tick" patternUnits="userSpaceOnUse" x="10" y="0" width="22.58" height="140">
      <rect x="0" y="129" width="0.9" height="11" fill="#1a1a1a"/>
    </pattern>
    <pattern id="inch-tick" patternUnits="userSpaceOnUse" x="10" y="0" width="90.32" height="140">
      <rect x="0" y="124" width="1" height="16" fill="#1a1a1a"/>
      <rect x="45.16" y="127" width="0.9" height="13" fill="#1a1a1a"/>
    </pattern>
  </defs>

  <rect class="ruler__body" x="0" y="0" width="1120" height="140"/>

  <g class="scale scale--metric">
    <rect x="8" y="0" width="1103" height="14" fill="url(#mm-tick)"/>
    <rect x="8" y="0" width="1103" height="14" fill="url(#half-cm-tick)"/>
    <rect x="8" y="0" width="1103" height="14" fill="url(#cm-tick)"/>
    <text class="scale-num" y="25">
      <tspan x="8.5">1</tspan><tspan x="44">2</tspan><tspan x="79.6">3</tspan><tspan x="115.2">4</tspan><tspan x="150.7">5</tspan><tspan x="186.3">6</tspan><tspan x="221.9">7</tspan><tspan x="257.4">8</tspan><tspan x="293">9</tspan><tspan x="328.5">10</tspan><tspan x="364.1">11</tspan><tspan x="399.7">12</tspan><tspan x="435.2">13</tspan><tspan x="470.8">14</tspan><tspan x="506.4">15</tspan><tspan x="541.9">16</tspan><tspan x="577.5">17</tspan><tspan x="613">18</tspan><tspan x="648.6">19</tspan><tspan x="684.2">20</tspan><tspan x="719.7">21</tspan><tspan x="755.3">22</tspan><tspan x="790.9">23</tspan><tspan x="826.4">24</tspan><tspan x="862">25</tspan><tspan x="897.5">26</tspan><tspan x="933.1">27</tspan><tspan x="968.7">28</tspan><tspan x="1004.2">29</tspan><tspan x="1039.8">30</tspan><tspan x="1075.4">31</tspan>
    </text>
  </g>

  <text class="headline" x="30" y="84">YOUR LOCAL GREASE TRAP AND LIQUID WASTE SPECIALISTS</text>

  <g class="contact">
    <rect class="contact-panel" x="772" y="29" width="348" height="73"/>

    <g class="brand">
      <circle class="brand-mark" cx="822" cy="48" r="12"/>
      <text class="brand-name" x="822" y="77">HARROWBY</text>
      <text class="brand-name" x="822" y="90">LIQUID WASTE</text>
    </g>

    <g class="contact-row" transform="translate(905 42)">
      <path class="contact-icon" d="M0 2.5c1 2.6 3 4.6 5.6 5.6l1.4-1.4 2.5 1v2.3c-5.6.3-10.4-4.5-10.1-10.1h2.3l1 2.5z"/>
      <text class="contact-text" x="16" y="9">08 8371 4925</text>
    </g>
    <g class="contact-row" transform="translate(905 58)">
      <rect class="contact-icon" x="0" y="1.5" width="9" height="6.5"/>
      <path class="contact-icon-detail" d="M0 1.5l4.5 3.5 4.5-3.5"/>
      <text class="contact-text" x="16" y="9">info@hdw.com.au</text>
    </g>
    <g class="contact-row" transform="translate(905 74)">
      <circle class="contact-icon" cx="4.5" cy="5" r="4.5"/>
      <path class="contact-icon-detail" d="M0 5h9M4.5 0.5v9"/>
      <text class="contact-text" x="16" y="9">www.harrowbyliquidwaste.com</text>
    </g>
  </g>

  <g class="scale scale--imperial">
    <rect x="10" y="122" width="1100" height="18" fill="url(#sixteenth-tick)"/>
    <rect x="10" y="122" width="1100" height="18" fill="url(#eighth-tick)"/>
    <rect x="10" y="122" width="1100" height="18" fill="url(#quarter-tick)"/>
    <rect x="10" y="122" width="1100" height="18" fill="url(#inch-tick)"/>
    <text class="scale-num scale-num--inch" y="119">
      <tspan x="15">1</tspan><tspan x="105.3">2</tspan><tspan x="195.6">3</tspan><tspan x="286">4</tspan><tspan x="376.3">5</tspan><tspan x="466.6">6</tspan><tspan x="556.9">7</tspan><tspan x="647.2">8</tspan><tspan x="737.6">9</tspan><tspan x="830">10</tspan><tspan x="920.3">11</tspan><tspan x="1010.6">12</tspan>
    </text>
  </g>
</svg>
</body>
</html>
```